I need a cover design for my lead-magnet (The Complete Atlas of C# Coder Toolkits) that will include a list of the most useful podcasts, courses, videos, conferences, groups, books, blogs, websites, repositories, tools, certifications and more.

My business is a membership that helps software developers using the C# programming language to master the language and become more productive (see these websites for more information https://my.brisktalon.net/, https://www.brisktalon.net/, https://www.brisktalon.net/membership/).

I believe images representing the categories I mentioned should visible on somehow interconnected on the cover.

I would like to convey the message of completeness and interconnectedness. I would like a beautiful colourful cover that makes me feel this eBook contains all the resources I care and need to progress in my career as a C# developer. I intend to use this eBook as my lead magnet so I want the cover to feel irresistible to new visitors. My logo and title should be visible on it.

Branding colors: #4D67A2 and #002140

I am open to creative and original designs so feel free to experiment with alternative ways of laying out the concepts as I shape in my mind what I want exactly.

Target Market(s)

C# Software Developers

Industry/Entity Type

Software Development

Font styles to use
Serif
Sans Serif

Colors

Designer to choose colors to be used in the design.

Requirements
Must have
• Image background with code/energy/electronic
• Small Title
• Logo
• Many images indicating the various categories the book contains (video icon, podcast icon, book icon, and so on) all somehow interconnected (alternatively each category could be it's own book and the entire cover will be a collection of books one for each category)
• 3D effect as a physical book with visible spine and pages
Nice to have
• Name (Vittoria Brunelli)
• Title/logo on the side of the book (3D effect)
Should not have
• Single colour background
• iPad

```html
<!DOCTYPE html>
<html lang="en">
<head>
<meta charset="utf-8">
<title>The Complete Atlas of C# Coder Toolkits — Cover</title>
<link rel="stylesheet" href="https://fonts.googleapis.com/css2?family=Arimo:wght@700&family=Tinos:wght@700&family=Roboto+Condensed:wght@700&display=swap">
<style>
  :root {
    --page-bg: #ffffff;
    --deep-navy: #002140;
    --brand-blue: #4D67A2;
    --electric: #1f5bff;
    --cyan-glow: #4fe3ff;
    --violet: #9a3cff;
    --title-yellow: #ffee00;
    --tag-red: #e8202c;
    --silver-light: #ffffff;
    --silver-dark: #8c95a6;
    --author-white: #f4f7ff;
  }
  * { margin: 0; padding: 0; box-sizing: border-box; }
  html, body { width: 1200px; height: 1002px; overflow: hidden; background: var(--page-bg); }

  .canvas { position: relative; width: 1200px; height: 1002px; }

  .cover {
    position: absolute; left: 265px; top: 31px;
    width: 670px; height: 940px; overflow: hidden;
    background: var(--deep-navy);
  }
  .cover-art { position: absolute; inset: 0; width: 100%; height: 100%; }

  .small-title {
    position: absolute; top: 150px; left: 0; width: 100%;
    text-align: center;
    font-family: "Arimo", Arial, sans-serif; font-weight: 700;
    font-size: 26px; line-height: 34px; color: var(--title-yellow);
    text-shadow: 0 0 3px #001a4a, 2px 2px 2px #001a4a;
  }

  .main-title {
    position: absolute; top: 270px; left: 0; width: 100%;
    text-align: center;
    font-family: "Tinos", "Times New Roman", serif; font-weight: 700;
  }
  .main-title .lang {
    display: block; font-size: 240px; line-height: 210px; letter-spacing: -6px;
    background: linear-gradient(180deg, var(--silver-light) 20%, #d9dee8 55%, var(--silver-dark) 100%);
    -webkit-background-clip: text; background-clip: text; color: transparent;
    filter: drop-shadow(3px 4px 3px rgba(0, 10, 40, .7));
  }
  .main-title .word {
    display: block; margin-top: 8px;
    font-size: 64px; line-height: 70px; color: var(--title-yellow);
    text-shadow: 2px 3px 3px rgba(0, 10, 50, .8);
  }

  .brand-mark {
    position: absolute; left: 38px; top: 712px;
    display: flex; flex-direction: column; align-items: center; gap: 6px;
  }
  .brand-mark .dot {
    width: 62px; height: 62px; border-radius: 50%;
    background: var(--brand-blue); border: 4px solid #ffffff;
  }
  .brand-mark .name {
    font-family: "Arimo", Arial, sans-serif; font-weight: 700;
    font-size: 17px; color: #ffffff;
  }

  .tagline {
    position: absolute; left: 212px; top: 718px;
    font-family: "Tinos", "Times New Roman", serif; font-weight: 700;
    font-size: 29px; line-height: 37px; color: var(--tag-red);
    -webkit-text-stroke: 1px #ffffff;
    text-shadow: 1px 2px 2px rgba(0, 0, 40, .6);
  }

  .category-icons {
    position: absolute; left: 52px; top: 866px;
    display: flex; gap: 14px; align-items: center;
  }
  .category-icons svg { width: 42px; height: 42px; }

  .author {
    position: absolute; right: 30px; top: 858px;
    font-family: "Roboto Condensed", "Arial Narrow", sans-serif; font-weight: 700;
    font-size: 27px; color: var(--author-white);
    text-shadow: 1px 2px 2px rgba(0, 0, 30, .8);
  }
</style>
</head>
<body>
<div class="canvas">
  <div class="cover">
    <svg class="cover-art" viewBox="0 0 670 940" role="img" aria-label="Electric blue code and circuit background with glowing rings and a burst of light">
      <defs>
        <linearGradient id="bg-fade" x1="0" y1="0" x2="0" y2="1">
          <stop offset="0" stop-color="#0a2f8f"/>
          <stop offset=".45" stop-color="#0b3cc4"/>
          <stop offset=".75" stop-color="#1b5df2"/>
          <stop offset="1" stop-color="#0d3fb8"/>
        </linearGradient>
        <radialGradient id="light-burst" cx=".5" cy=".74" r=".55">
          <stop offset="0" stop-color="#ffffff"/>
          <stop offset=".12" stop-color="#8ff3ff" stop-opacity=".9"/>
          <stop offset=".4" stop-color="#2f9bff" stop-opacity=".4"/>
          <stop offset="1" stop-color="#1b5df2" stop-opacity="0"/>
        </radialGradient>
        <radialGradient id="ring-core" cx=".5" cy=".5" r=".5">
          <stop offset="0" stop-color="#0f5fe0"/>
          <stop offset=".7" stop-color="#2a2bb8"/>
          <stop offset="1" stop-color="#5a1fb0"/>
        </radialGradient>
        <linearGradient id="code-haze" x1="0" y1="0" x2="0" y2="1">
          <stop offset="0" stop-color="#35e0ff" stop-opacity=".35"/>
          <stop offset="1" stop-color="#35e0ff" stop-opacity="0"/>
        </linearGradient>
      </defs>
      <rect width="670" height="940" fill="url(#bg-fade)"/>
      <rect width="670" height="320" fill="url(#code-haze)"/>
      <circle cx="349" cy="440" r="232" fill="none" stroke="#2b7dff" stroke-width="3" opacity=".6"/>
      <circle cx="349" cy="440" r="200" fill="url(#ring-core)"/>
      <circle cx="349" cy="440" r="200" fill="none" stroke="var(--cyan-glow)" stroke-width="12" opacity=".9"/>
      <circle cx="349" cy="440" r="172" fill="none" stroke="var(--violet)" stroke-width="6" opacity=".8"/>
      <circle cx="349" cy="440" r="120" fill="none" stroke="#47b4ff" stroke-width="2" opacity=".5"/>
      <rect width="670" height="940" fill="url(#light-burst)"/>
    </svg>

    <h2 class="small-title">The Complete Atlas of<br>C# Coder Toolkits</h2>

    <h1 class="main-title">
      <span class="lang">C#</span>
      <span class="word">Programming</span>
    </h1>

    <div class="brand-mark">
      <span class="dot"></span>
      <span class="name">Brisktalon</span>
    </div>

    <p class="tagline">A very informative book<br>on Programming World</p>

    <div class="category-icons">
      <svg viewBox="0 0 42 42" aria-label="Videos" role="img">
        <rect x="2" y="7" width="38" height="28" rx="3" fill="#e3121b"/>
        <path d="M17 14 L28 21 L17 28 Z" fill="#ffffff"/>
      </svg>
      <svg viewBox="0 0 42 42" aria-label="Podcasts" role="img">
        <circle cx="21" cy="18" r="15" fill="none" stroke="#ffe100" stroke-width="3"/>
        <rect x="16" y="10" width="10" height="16" rx="5" fill="#ffe100"/>
        <rect x="19" y="27" width="4" height="12" fill="#ffe100"/>
      </svg>
      <svg viewBox="0 0 42 42" aria-label="Websites" role="img">
        <circle cx="21" cy="21" r="17" fill="none" stroke="#ffffff" stroke-width="2.5"/>
        <ellipse cx="21" cy="21" rx="8" ry="17" fill="none" stroke="#ffffff" stroke-width="2"/>
        <line x1="4" y1="21" x2="38" y2="21" stroke="#ffffff" stroke-width="2"/>
        <line x1="7" y1="12" x2="35" y2="12" stroke="#ffffff" stroke-width="2"/>
        <line x1="7" y1="30" x2="35" y2="30" stroke="#ffffff" stroke-width="2"/>
      </svg>
      <svg viewBox="0 0 42 42" aria-label="Books" role="img">
        <rect x="6" y="6" width="30" height="12" fill="#8a3b12"/>
        <rect x="4" y="20" width="34" height="8" fill="#c0392b"/>
        <rect x="4" y="30" width="34" height="8" fill="#f1f1f1"/>
      </svg>
    </div>

    <p class="author">Vittoria Brunelli</p>
  </div>
</div>
</body>
</html>
```